Bakery Business Cards

We are in need of business cards for our bakery business--something non-generic that reflects our business and will stand out. We are a wholesale bakery that primarily services in-store bakeries, casinos, schools, distributors, and fund-raising companies. The family business was founded in 1960. (www.marlowsovenworks.com)

```html
<!DOCTYPE html>
<html lang="en">
<head>
<meta charset="utf-8">
<title>Marlow's Ovenworks – Business Cards</title>
<link href="https://fonts.googleapis.com/css2?family=Courgette&display=swap" rel="stylesheet">
<style>
  :root {
    --cocoa: #1c0a0c;
    --crust: #d59c78;
    --crust-deep: #b9825f;
    --cream: #ffffff;
    --page: #ffffff;
    --wood-light: #dcbb8c;
    --wood-mid: #c99f6c;
  }
  * { margin: 0; padding: 0; box-sizing: border-box; }
  html, body {
    width: 1200px; height: 1000px; overflow: hidden;
    background: var(--page);
    font-family: "Courgette", cursive;
  }
  .canvas { position: relative; width: 1200px; height: 1000px; }
  .card {
    position: absolute; left: 318px; width: 590px; height: 389px;
    overflow: hidden;
    box-shadow: 6px 8px 10px rgba(0,0,0,0.35);
  }
  .card--front { top: 83px; }
  .card--back { top: 496px; height: 390px; }
  .card-art { position: absolute; inset: 0; width: 100%; height: 100%; }

  .brand-name {
    position: absolute; color: var(--cream);
    font-size: 34px; line-height: 1; text-align: center; white-space: nowrap;
  }
  .tagline {
    position: absolute; color: var(--cream);
    font-size: 17px; line-height: 1; text-align: center; white-space: nowrap;
  }
  .card--front .brand-name { left: 0; right: 0; top: 180px; }
  .card--front .tagline { left: 0; right: 0; top: 249px; }
  .website {
    position: absolute; left: 0; width: 560px; top: 338px;
    text-align: center; color: var(--cocoa); font-size: 18px; line-height: 1;
  }

  .card--back .brand-name { left: 250px; width: 340px; top: 96px; font-size: 32px; }
  .card--back .tagline { left: 250px; width: 340px; top: 171px; }
  .contact-list { position: absolute; left: 316px; top: 220px; list-style: none; }
  .contact-item {
    display: flex; align-items: center; gap: 8px;
    color: var(--crust); font-size: 11px; line-height: 1.3;
    margin-bottom: 14px;
  }
  .contact-icon { width: 20px; height: 20px; flex: none; }
</style>
</head>
<body>
<main class="canvas">

  <section class="card card--front">
    <svg class="card-art" viewBox="0 0 590 389" preserveAspectRatio="none">
      <rect width="590" height="389" fill="var(--crust)"/>
      <rect role="img" aria-label="Sketched lattice pie crust illustration" x="0" y="0" width="162" height="78" fill="var(--crust-deep)"/>
      <rect role="img" aria-label="Sketched lattice pie crust illustration" x="428" y="310" width="162" height="79" fill="var(--crust-deep)"/>
      <path d="M0 22 Q295 150 590 22 L590 345 Q295 255 0 345 Z" fill="var(--cocoa)"/>
    </svg>
    <div class="brand-name">Marlow's Ovenworks</div>
    <div class="tagline">Baked Fresh for Every Table</div>
    <div class="website">www.marlowsovenworks.com</div>
  </section>

  <section class="card card--back">
    <svg class="card-art" viewBox="0 0 590 390" preserveAspectRatio="none">
      <defs>
        <linearGradient id="pie-photo" x1="0" y1="0" x2="1" y2="1">
          <stop offset="0" stop-color="var(--wood-light)"/>
          <stop offset="0.45" stop-color="var(--wood-mid)"/>
          <stop offset="1" stop-color="var(--wood-light)"/>
        </linearGradient>
      </defs>
      <rect role="img" aria-label="Photo of cherry and berry pie slices in white bowls on a wooden table" width="590" height="390" fill="url(#pie-photo)"/>
      <rect x="250" y="0" width="340" height="34" fill="var(--crust)"/>
      <path d="M262 32 Q225 170 232 342 L590 342 L590 32 Z" fill="var(--cocoa)"/>
      <rect x="422" y="342" width="168" height="48" fill="var(--crust)"/>
    </svg>
    <div class="brand-name">Marlow's Ovenworks</div>
    <div class="tagline">Baked Fresh for Every Table</div>
    <ul class="contact-list">
      <li class="contact-item">
        <svg class="contact-icon" viewBox="0 0 20 20"><circle cx="10" cy="10" r="10" fill="var(--crust)"/><path d="M7 5.5 L8.6 7.6 L7.8 8.8 Q9 11.2 11.2 12.2 L12.4 11.4 L14.5 13 L13.4 14.6 Q9.5 14.4 6.4 10 Q5.4 7.2 7 5.5 Z" fill="var(--cocoa)"/></svg>
        <span>405.555.0148</span>
      </li>
      <li class="contact-item">
        <svg class="contact-icon" viewBox="0 0 20 20"><circle cx="10" cy="10" r="10" fill="var(--crust)"/><path d="M10 4.5 A4 4 0 0 1 14 8.5 Q14 11 10 15.5 Q6 11 6 8.5 A4 4 0 0 1 10 4.5 Z" fill="var(--cocoa)"/><circle cx="10" cy="8.5" r="1.5" fill="var(--crust)"/></svg>
        <span>Marlow's Ovenworks, Inc. 1187 Harbor Ave<br>Tulsa, OK 74103</span>
      </li>
      <li class="contact-item">
        <svg class="contact-icon" viewBox="0 0 20 20"><circle cx="10" cy="10" r="10" fill="var(--crust)"/><rect x="5" y="6.5" width="10" height="7" fill="var(--cocoa)"/><path d="M5 6.5 L10 10.5 L15 6.5" fill="none" stroke="var(--crust)" stroke-width="0.9"/></svg>
        <span>contact@marlowsovenworks.com</span>
      </li>
    </ul>
  </section>

</main>
</body>
</html>
```